Non-profit sports organization needs templates for Word and InDesign

"Fralo Teens" is a non-profit organization in Winterthur, which supports the recruitment of young talent by the handball clubs in Winterthur. Every year we run several camps, a tournament for schoolchildren and several handball lessons at school.
During these activities there are always written information. So far we have not given much thought to the design. But since we think that a professional design will also lead to more interaction, we now turn to you as a designer.

For the communication with partners, sponsors, patrons, etc. we need a uniform appearance. Since different departments are currently working with different programs, we need a template for letters and documentation for Word and InDesign.

We will need the documentation template for project descriptions, information, etc.
The letter templates are needed to contact sponsors, authorities, patrons, etc.

Both the letter template and the documentation template should look modern. The design should be based on the existing flyers. Otherwise we have no other requirements so far.

Homepage: www.fralo-teens.ch

Target Market(s)

Letters, documentation or information to authorities, sponsors, associations, patrons, members, participants, etc.

Requirements
Must have
• In addition to the design, the templates should also contain a concept for titles, paragraphs, lists, etc. (colors / fonts / ...)

Word and Indesign templates

```html
<!DOCTYPE html>
<html lang="en">
<head>
<meta charset="utf-8">
<title>Fralo Teens – Letter Template</title>
<link rel="stylesheet" href="https://fonts.googleapis.com/css2?family=Arimo:wght@400;700&display=swap">
<style>
  :root {
    --navy: #25408f;
    --sky: #079ad6;
    --pale: #c6e8f8;
    --mist: #dff1fb;
    --ink: #1d1d1b;
    --paper: #ffffff;
    --brand-red: #e52d27;
  }
  * { margin: 0; padding: 0; box-sizing: border-box; }
  html, body { width: 848px; height: 1200px; overflow: hidden; background: var(--paper); }
  body { font-family: "Arimo", Arial, sans-serif; color: var(--ink); }
  .letter { position: relative; width: 848px; height: 1200px; overflow: hidden; }
  .decor { position: absolute; inset: 0; width: 848px; height: 1200px; }
  .letter-title {
    position: absolute; left: 86px; top: 86px;
    font-size: 33.5px; font-weight: 400; color: var(--paper); line-height: 1.1;
  }
  .brand {
    position: absolute; left: 628px; top: 130px;
    display: flex; align-items: center; gap: 8px;
  }
  .brand-dot { width: 22px; height: 22px; border-radius: 50%; background: var(--brand-red); }
  .brand-name { font-size: 25px; font-weight: 400; color: var(--sky); }
  .content { position: absolute; left: 86px; top: 413px; width: 686px; }
  .salutation { font-size: 15.5px; font-weight: 700; margin-bottom: 13px; }
  .body-text p { font-size: 13px; line-height: 15.5px; margin-bottom: 15.5px; hyphens: auto; -webkit-hyphens: auto; }
  .signature { position: absolute; left: 86px; top: 817px; font-size: 13px; }
  .footer-contact {
    position: absolute; left: 542px; top: 1154px;
    font-size: 11.2px; color: var(--paper);
  }
</style>
</head>
<body>
<main class="letter">
  <svg class="decor" viewBox="0 0 1240 1754" preserveAspectRatio="none" aria-hidden="true">
    <polygon fill="var(--pale)" points="0,66 420,0 1240,0 1240,80 596,162 0,290"/>
    <polygon fill="var(--sky)" points="0,236 50,222 596,266 0,404"/>
    <polygon fill="var(--navy)" points="0,68 596,98 596,266 52,235 0,118"/>
    <polygon fill="var(--mist)" points="0,1726 1240,1648 1240,1754 0,1754"/>
    <polygon fill="var(--navy)" points="776,1658 1240,1658 1240,1754 710,1754"/>
  </svg>

  <h1 class="letter-title">Title Here</h1>

  <div class="brand">
    <span class="brand-dot"></span>
    <span class="brand-name">Fralo Teens</span>
  </div>

  <section class="content">
    <p class="salutation">Ebis eaturib,</p>
    <div class="body-text">
      <p>Ditam que vellibus. Aximolo restem lautem repero eos pro qui bea volores ectiatur, si tempelis eate velecae preribus molor sint impos dolore vel iminctatia destis mo te venti cullaccumeni cum et que voluptis doluptae nobit, ullis maion pe non nime vel ipsuntiunt dignatem faces etus volesto tem volorat qui destis ma sundandi odistiaes rerferum et adipsa nonse et la coneture corepti onecatinimin conse incillo rehenia core nostori autemod isquia dolorum repreptatis apis sapit et fugitia cum idendellabo. Pa sum ilibus sum que parum et maior si arci reres eum acculla ccaborp oreris et rerchiciet, voleceped que dunt quiat.</p>
      <p>Edigni qui illati tem et litiis ad quas sus non comnima gnimi, corepedit, sitio quundig natem. Nequasitibus aut volenih icipsa doloria im audam que parchit volupta tiatus dolorro in rempore perupitat doluptas adiorepre corro testis nis dolorero eum ius ni volum int.</p>
      <p>Adis si ni dolorep elenditatis ma nullaccum esed molupta dolorunto discipit dis aut ligenih itibus eos quiae volorita is apidus erci aciliamus nus dolorum nis magniet vent inis modis el maio. Te perfera tiassim facid que esequo offic tet quia voluptatem laborpo rrovit etus aut ipsandio ommolo dionem fugitatis perrovid que voles si vent iusanimi, quo endis esequat adit, consequibus eosam quid modit, od maximporit veleseque modistibus eaquissi sandem et voluptati doluptumeaquam, comnis dolupic te nimagnamet qui is eatis excessi tatempo riore, con repedi que latemquos int re imus, quam sim expereperum hillit lanim ea inveriorum necum iur, consequo discilitem hitium quiditisti comnisi te non rem qui quidebit explit aut repelest, omnis apitatemque dent min rerio. Et quatur, sitas et im que qui secea verehent pera cus doluptae pratur reium net miniaectis sum iliqui omnim ut quos il ilitatium et utae aut magnis endis imin nonsenda dio eum at vel im sita voluptatur, offic to berum sit harum ut ea nobit quia adi repelenia dolores et.</p>
    </div>
  </section>

  <p class="signature">Maximporit Veleseque</p>

  <p class="footer-contact">Address: 5312 Talwil | Email: info@fralo-teens.ch</p>
</main>
</body>
</html>
```